Data Analysis new tech startup

Design a simple / modern website (one page, one language) with a tech touch, based on the words prediction and/or IoT (Internet of Things).

VOLTEQ IoT is dedicated for Data Analysis of IoT or M2M (Machine to Machine) projects.

The website should follow the colors of the logo (see images)

The web site should look like this example: https://malvira-systems.example/en/ with less human pictures and ALL the text content should be configurable for later change.

The website will be published on a php web server.

Target Market(s)

Business professionals

Industry/Entity Type

Data Science

Coding

Coded - Design and coding required

Number of Pages Required

1 page

Colors

Designer to choose colors to be used in the design.

Requirements
Must have
• Follow example site guidelines (https://malvira-systems.example/en/)
• Follow logo colors
• Fun and startup look and feel
• ALL TEXT SHOULD BE CONFIGURABLE
• Clients carrousel with colored hovering
Nice to have
• Configurable photo carrousel at the top (after menu)
Should not have
• Too many human photos, just a few.

```html
<!DOCTYPE html>
<html lang="en">
<head>
<meta charset="utf-8">
<title>VOLTEQ IoT — Data Analysis</title>
<link rel="stylesheet" href="https://fonts.googleapis.com/css2?family=Montserrat:wght@400;500;600;700;800&display=swap">
<style>
  :root {
    --violet-deep: #5a1fd4;
    --violet: #7b2fe6;
    --indigo: #4f4fe8;
    --blue: #3d84f6;
    --heading-blue: #3c5fe0;
    --pink: #e8306a;
    --magenta: #c22fd8;
    --text: #6b6f80;
    --line: #e7e9f0;
    --white: #ffffff;
    --page: #f6f6f8;
  }
  * { box-sizing: border-box; margin: 0; padding: 0; }
  html, body { width: 1200px; height: 4202px; overflow: hidden; }
  body { font-family: "Montserrat", sans-serif; background: var(--white); color: var(--text); }
  section, footer { position: relative; width: 1200px; overflow: hidden; }
  .abs { position: absolute; }

  /* brand name: plain text only */
  .brand-name { color: var(--white); font-weight: 700; font-size: 26px; letter-spacing: .5px; white-space: nowrap; }

  /* hero */
  .hero { height: 720px; background: linear-gradient(100deg, var(--indigo) 0%, var(--violet-deep) 55%, var(--violet) 100%); }
  .hero .brand-name { left: 92px; top: 46px; }
  .nav { right: 92px; top: 54px; display: flex; gap: 52px; font-size: 12px; font-weight: 500; color: var(--white); }
  .nav .active { color: var(--pink); display: flex; align-items: center; gap: 8px; }
  .nav .active::before { content: ""; width: 28px; height: 1.5px; background: var(--pink); }
  .hero-rule { left: 92px; top: 200px; width: 1px; height: 330px; background: rgba(255,255,255,.4); }
  .scroll-down { left: 78px; top: 470px; transform: rotate(-90deg); transform-origin: left top; font-size: 8px; letter-spacing: 2px; color: rgba(255,255,255,.8); white-space: nowrap; }
  .hero-title { left: 118px; top: 220px; color: var(--white); font-weight: 800; font-size: 72px; line-height: 1; letter-spacing: 1px; }
  .hero-lead { left: 118px; top: 390px; width: 340px; color: var(--white); font-size: 15px; line-height: 1.5; font-weight: 500; }
  .hero-dots { left: 178px; top: 495px; display: flex; gap: 6px; align-items: center; }
  .hero-dots span { width: 4px; height: 4px; border-radius: 50%; background: rgba(255,255,255,.6); }
  .hero-dots span.on { width: 6px; height: 6px; background: var(--white); }
  .hero-art { left: 560px; top: 150px; width: 420px; height: 380px; border-radius: 30px; background: radial-gradient(circle at 50% 45%, rgba(125,200,255,.55), rgba(120,80,240,.25) 60%, rgba(120,80,240,0) 75%); }
  .hero-wave { left: 0; bottom: 0; }

  /* headings */
  .section-title { display: flex; align-items: center; gap: 10px; color: var(--heading-blue); font-size: 34px; font-weight: 500; letter-spacing: .5px; }
  .section-title .mark { width: 22px; height: 22px; border-radius: 50%; border: 5px solid var(--heading-blue); }
  .on-color .section-title { color: var(--white); }
  .on-color .section-title .mark { border-color: var(--white); }
  .intro { font-size: 11px; line-height: 1.7; text-align: center; color: var(--text); }

  /* methodology */
  .methodology { height: 700px; }
  .methodology .section-title { left: 0; right: 0; top: 90px; justify-content: center; }
  .methodology .intro { left: 300px; width: 600px; top: 165px; }
  .steps { left: 179px; top: 300px; display: flex; gap: 127px; }
  .step { width: 115px; text-align: center; }
  .step-card { width: 115px; height: 115px; border: 1px solid var(--line); border-radius: 14px 14px 40px 14px; display: flex; align-items: center; justify-content: center; background: var(--white); }
  .step-card.is-active { border: none; background: linear-gradient(135deg, var(--blue), var(--violet)); box-shadow: 0 12px 24px rgba(90,60,230,.3); }
  .step-name { margin-top: 28px; color: var(--pink); font-size: 11px; font-weight: 700; }
  .step-text { margin: 14px -36px 0; font-size: 10px; line-height: 1.6; color: var(--text); }

  /* company */
  .company { height: 700px; background: linear-gradient(180deg, var(--white), var(--page)); }
  .company .section-title { left: 92px; top: 120px; }
  .company-text { left: 92px; top: 200px; width: 350px; font-size: 10.5px; line-height: 1.75; }
  .company-rings { left: 620px; top: 70px; width: 440px; height: 440px; border-radius: 50%; border: 1px solid var(--line); }
  .company-art { left: 680px; top: 130px; width: 320px; height: 320px; border-radius: 50%; background: radial-gradient(circle at 50% 50%, #6a7bf0 0%, #9c8cf5 45%, #eef0fb 75%); box-shadow: 0 20px 40px rgba(100,110,180,.18); }

  /* offering */
  .offering { height: 600px; background: linear-gradient(100deg, var(--blue) 0%, #5a6cf0 50%, var(--violet) 100%); }
  .offering-notch { left: 560px; top: -1px; }
  .offering .section-title { left: 0; right: 0; top: 90px; justify-content: center; }
  .offering .intro { left: 290px; width: 620px; top: 165px; color: rgba(255,255,255,.9); }
  .services { left: 330px; top: 255px; display: flex; gap: 80px; }
  .service { width: 130px; text-align: center; color: var(--white); font-size: 14px; font-weight: 500; line-height: 1.3; }
  .service-ring { width: 120px; height: 120px; margin: 0 auto 18px; border-radius: 50%; border: 2px solid rgba(255,255,255,.35); display: flex; align-items: center; justify-content: center; }
  .service-icon { width: 94px; height: 94px; border-radius: 50%; display: flex; align-items: center; justify-content: center; }
  .is-red { background: var(--pink); }
  .is-magenta { background: var(--magenta); }
  .is-blue { background: var(--blue); }

  /* join */
  .join { height: 700px; }
  .join-rings { left: 150px; top: 120px; width: 440px; height: 440px; border-radius: 50%; border: 1px solid var(--line); }
  .join-art { left: 215px; top: 185px; width: 310px; height: 310px; border-radius: 50%; background: radial-gradient(circle at 50% 50%, #3a1a8a 0%, var(--magenta) 22%, #f1d7f5 55%, var(--white) 72%); box-shadow: 0 16px 40px rgba(120,110,170,.18); }
  .join-title { left: 655px; top: 210px; color: var(--heading-blue); font-size: 32px; font-weight: 500; letter-spacing: 1px; }
  .join-text { left: 655px; top: 270px; width: 360px; font-size: 10.5px; line-height: 1.75; }
  .button { display: inline-block; background: var(--heading-blue); color: var(--white); font-size: 13px; font-weight: 600; padding: 10px 20px; border-radius: 4px 4px 16px 4px; }
  .join .button { left: 655px; top: 370px; }

  /* partners */
  .partners { height: 380px; }
  .partners .section-title { left: 0; right: 0; top: 40px; justify-content: center; }
  .partner-row { left: 230px; top: 150px; display: flex; gap: 95px; align-items: center; }
  .partner-badge { width: 68px; height: 68px; background: #c9ccd4; }
  .partner-badge.round { border-radius: 50%; }
  .partner-badge.rounded { border-radius: 14px; }
  .partner-badge.diamond { transform: rotate(45deg) scale(.8); border-radius: 8px; }

  /* footer */
  .footer { height: 402px; }
  .footer-wave { left: 0; top: 0; }
  .footer .brand-name { left: 92px; top: 160px; font-size: 40px; }
  .social { left: 92px; top: 245px; display: flex; gap: 8px; }
  .social span { width: 26px; height: 26px; border-radius: 50%; background: var(--white); }
  .copyright { left: 92px; top: 315px; font-size: 9px; color: rgba(255,255,255,.9); }
  .col-title { font-size: 12px; font-weight: 600; letter-spacing: .5px; color: var(--white); }
  .contact { left: 515px; top: 150px; width: 230px; }
  .contact-line { display: flex; gap: 8px; margin-top: 16px; font-size: 9.5px; line-height: 1.6; color: rgba(255,255,255,.9); }
  .contact-line svg { flex: none; margin-top: 2px; }
  .touch { left: 790px; top: 150px; width: 210px; }
  .field { margin-top: 12px; height: 26px; border: 1px solid rgba(255,255,255,.6); font-size: 8.5px; color: rgba(255,255,255,.8); padding: 7px 10px; }
  .submit { margin-top: 12px; display: inline-block; background: var(--white); color: var(--violet); font-size: 11px; font-weight: 600; padding: 5px 18px; border-radius: 4px 4px 12px 4px; }
</style>
</head>
<body>

<section class="hero">
  <div class="abs brand-name">VOLTEQ IoT</div>
  <nav class="abs nav">
    <span class="active">Home</span><span>Our Methodology</span><span>Our Offering</span><span>Careers</span><span>Contact</span>
  </nav>
  <div class="abs hero-rule"></div>
  <div class="abs scroll-down">SCROLL DOWN</div>
  <h1 class="abs hero-title">DATA<br>ANALYSIS</h1>
  <p class="abs hero-lead">Lorem ipsum dolor sit amet, consectetur adipiscing elit.</p>
  <div class="abs hero-dots"><span></span><span class="on"></span><span></span></div>
  <div class="abs hero-art" role="img" aria-label="Isometric illustration of a data server linked to laptops and code screens"></div>
  <svg class="abs hero-wave" width="1200" height="140" viewBox="0 0 1200 140" aria-hidden="true">
    <path d="M0 140 L0 70 C220 0 420 20 640 60 C880 104 1060 100 1200 30 L1200 140 Z" fill="#ffffff"/>
  </svg>
</section>

<section class="methodology">
  <h2 class="abs section-title"><span class="mark"></span>OUR METHODOLOGY</h2>
  <p class="abs intro">Lorem ipsum dolor sit amet, consectetur adipiscing elit. Aenean eu faucibus augue. Nullam vel suscipit augue. Morbi sit amet faucibus elit, nec dignissim augue. Lorem ipsum dolor sit amet, consectetur adipiscing elit.</p>
  <div class="abs steps">
    <div class="step">
      <div class="step-card">
        <svg width="52" height="40" viewBox="0 0 52 40" aria-hidden="true"><path d="M4 6h20v30H4zM28 6h20v30H28z" fill="none" stroke="#3c5fe0" stroke-width="3"/><path d="M8 13h12M8 19h12M8 25h12M32 13h12M32 19h12M32 25h12" stroke="#3c5fe0" stroke-width="2"/></svg>
      </div>
      <div class="step-name">LEARN</div>
      <p class="step-text">Lorem ipsum dolor sit amet, consectetur adipiscing elit. Aenean eu faucibus augue.</p>
    </div>
    <div class="step">
      <div class="step-card is-active">
        <svg width="44" height="44" viewBox="0 0 44 44" aria-hidden="true"><rect x="6" y="10" width="32" height="22" rx="2" fill="none" stroke="#fff" stroke-width="3"/><path d="M16 38h12M22 32v6" stroke="#fff" stroke-width="3"/><rect x="14" y="16" width="16" height="10" fill="#fff" opacity=".6"/></svg>
      </div>
      <div class="step-name">APPLY</div>
      <p class="step-text">Lorem ipsum dolor sit amet, consectetur adipiscing elit. Aenean eu faucibus augue.</p>
    </div>
    <div class="step">
      <div class="step-card">
        <svg width="48" height="48" viewBox="0 0 48 48" aria-hidden="true"><circle cx="16" cy="30" r="9" fill="none" stroke="#3c5fe0" stroke-width="4" stroke-dasharray="4 3"/><circle cx="32" cy="16" r="9" fill="none" stroke="#3c5fe0" stroke-width="4" stroke-dasharray="4 3"/><circle cx="16" cy="30" r="3" fill="#3c5fe0"/><circle cx="32" cy="16" r="3" fill="#3c5fe0"/></svg>
      </div>
      <div class="step-name">IMPLEMENT</div>
      <p class="step-text">Lorem ipsum dolor sit amet, consectetur adipiscing elit. Aenean eu faucibus augue.</p>
    </div>
    <div class="step">
      <div class="step-card">
        <svg width="52" height="40" viewBox="0 0 52 40" aria-hidden="true"><rect x="8" y="4" width="36" height="24" rx="2" fill="none" stroke="#3c5fe0" stroke-width="3"/><path d="M2 34h48" stroke="#3c5fe0" stroke-width="4"/><circle cx="26" cy="16" r="6" fill="none" stroke="#3c5fe0" stroke-width="2.5"/></svg>
      </div>
      <div class="step-name">MANAGE</div>
      <p class="step-text">Lorem ipsum dolor sit amet, consectetur adipiscing elit. Aenean eu faucibus augue.</p>
    </div>
  </div>
</section>

<section class="company">
  <h2 class="abs section-title"><span class="mark"></span>OUR COMPANY</h2>
  <p class="abs company-text">Morbi vel massa faucibus, aliquam ante vitae, egestas est. Duis ut convallis diam. Aliquam laoreet, tortor nec rhoncus imperdiet, arcu nisi euismod ante, aliquam mattis leo libero sed nulla. Fusce ultricies semper dolor, consequat fermentum est faucibus id. Proin mauris nisi, euismod in mollis vitae, finibus ac lectus. Nullam sed est rutrum, tincidunt diam a, lacinia dolor. Phasellus non pretium ante. Curabitur accumsan justo et mi ullamcorper ultricies ut id orci. Morbi laoreet scelerisque tincidunt. Praesent faucibus ultricies iaculis. Nam eget tortor cursus, rhoncus ante sed, tristique lacus. Vestibulum posuere commodo tempus. Quisque ac fermentum velit. Nullam non fringilla nisi.</p>
  <div class="abs company-rings"></div>
  <div class="abs company-art" role="img" aria-label="Illustration of a developer working at tall code screens with gears, a cloud and a padlock"></div>
</section>

<section class="offering on-color">
  <svg class="abs offering-notch" width="80" height="22" viewBox="0 0 80 22" aria-hidden="true"><path d="M0 0 H80 C60 0 50 18 40 18 C30 18 20 0 0 0 Z" fill="#f6f6f8"/><path d="M34 10 L40 5 L46 10" fill="none" stroke="#3c5fe0" stroke-width="1.5"/></svg>
  <h2 class="abs section-title"><span class="mark"></span>OUR OFFERING</h2>
  <p class="abs intro">Morbi vel massa faucibus, aliquam ante vitae, egestas est. Duis ut convallis diam. Aliquam laoreet, tortor nec rhoncus imperdiet, arcu nisi euismod ante, aliquam mattis leo libero sed nulla. Fusce ultricies semper dolor, consequat fermentum est faucibus id.</p>
  <div class="abs services">
    <div class="service">
      <div class="service-ring"><div class="service-icon is-red">
        <svg width="40" height="40" viewBox="0 0 40 40" aria-hidden="true"><circle cx="13" cy="12" r="5" fill="#fff"/><circle cx="27" cy="12" r="5" fill="#fff"/><rect x="6" y="20" width="14" height="14" rx="3" fill="#fff"/><rect x="20" y="20" width="14" height="14" rx="3" fill="#fff"/></svg>
      </div></div>
      Consulting<br>&amp; Implementation
    </div>
    <div class="service">
      <div class="service-ring"><div class="service-icon is-magenta">
        <svg width="40" height="40" viewBox="0 0 40 40" aria-hidden="true"><circle cx="20" cy="15" r="8" fill="none" stroke="#fff" stroke-width="4" stroke-dasharray="4 3"/><path d="M4 26 L14 34 H26 L36 26" fill="none" stroke="#fff" stroke-width="3"/></svg>
      </div></div>
      Reseach<br>&amp; Development
    </div>
    <div class="service">
      <div class="service-ring"><div class="service-icon is-blue">
        <svg width="42" height="40" viewBox="0 0 42 40" aria-hidden="true"><rect x="12" y="5" width="26" height="18" fill="none" stroke="#fff" stroke-width="3"/><circle cx="8" cy="10" r="4" fill="#fff"/><circle cx="14" cy="30" r="3.5" fill="#fff"/><circle cx="22" cy="30" r="3.5" fill="#fff"/><circle cx="30" cy="30" r="3.5" fill="#fff"/></svg>
      </div></div>
      Training<br>&amp; Coaching
    </div>
  </div>
</section>

<section class="join">
  <div class="abs join-rings"></div>
  <div class="abs join-art" role="img" aria-label="Large decorative emblem in magenta, pink and deep blue"></div>
  <h2 class="abs join-title">JOIN&nbsp; VOLTEQ-IOT</h2>
  <p class="abs join-text">Morbi vel massa faucibus, aliquam ante vitae, egestas est. Duis ut convallis diam. Aliquam laoreet, tortor nec rhoncus imperdiet, arcu nisi euismod ante, aliquam mattis leo libero sed nulla. Fusce ultricies semper dolor, consequat fermentum est faucibus id.</p>
  <span class="abs button">Apply Now</span>
</section>

<section class="partners">
  <h2 class="abs section-title"><span class="mark"></span>OUR PARTNER</h2>
  <div class="abs partner-row">
    <span class="partner-badge round" role="img" aria-label="Partner badge"></span>
    <span class="partner-badge rounded" role="img" aria-label="Partner badge"></span>
    <span class="partner-badge round" role="img" aria-label="Partner badge"></span>
    <span class="partner-badge round" role="img" aria-label="Partner badge"></span>
    <span class="partner-badge diamond" role="img" aria-label="Partner badge"></span>
  </div>
</section>

<footer class="footer">
  <svg class="abs footer-wave" width="1200" height="402" viewBox="0 0 1200 402" aria-hidden="true">
    <defs><linearGradient id="footerFill" x1="0" x2="1" y1="0" y2="0"><stop offset="0" stop-color="#3d84f6"/><stop offset="1" stop-color="#7b2fe6"/></linearGradient></defs>
    <path d="M0 80 C200 20 420 40 620 90 C840 140 1020 100 1200 0 L1200 402 L0 402 Z" fill="url(#footerFill)"/>
  </svg>
  <div class="abs brand-name">VOLTEQ IoT</div>
  <div class="abs social"><span></span><span></span><span></span><span></span></div>
  <p class="abs copyright">Copyright © 2019 VOLTEQ-IoT. All Rights Reserved.</p>
  <div class="abs contact">
    <div class="col-title">CONTACT WITH US</div>
    <div class="contact-line"><svg width="10" height="12" viewBox="0 0 10 12" aria-hidden="true"><path d="M5 0a4 4 0 0 1 4 4c0 3-4 8-4 8S1 7 1 4a4 4 0 0 1 4-4z" fill="#fff"/></svg><span>Morbi vel massa faucibus, aliquam ante vitae, egestas est. Duis ut convallis diam.</span></div>
    <div class="contact-line"><svg width="10" height="10" viewBox="0 0 10 10" aria-hidden="true"><path d="M2 0h2l1 3-1.5 1a6 6 0 0 0 2.5 2.5L7 5l3 1v2c0 1-1 2-2 2A8 8 0 0 1 0 2c0-1 1-2 2-2z" fill="#fff"/></svg><span>+61 (0) 1 5550 0142</span></div>
    <div class="contact-line"><svg width="10" height="10" viewBox="0 0 10 10" aria-hidden="true"><circle cx="5" cy="5" r="5" fill="#fff"/><path d="M2.5 3.5h5v3h-5zM2.5 3.5 5 5.5l2.5-2" fill="none" stroke="#6b5ef0" stroke-width=".8"/></svg><span>info@volteqiot.example</span></div>
  </div>
  <div class="abs touch">
    <div class="col-title">GET IN TOUCH</div>
    <div class="field">Enter Name</div>
    <div class="field">Enter Email</div>
    <span class="submit">Submit</span>
  </div>
</footer>

</body>
</html>
```